Premium Wagyu Smallgoods Packaging Design (A5)

Hi there,
We are Ember Ridge Wagyu; a wagyu beef company based in Christchurch, New Zealand. We are needing new packaging for our new line of wagyu smallgoods (salami, braesola, fina seca etc.).
About us: Ember Ridge Wagyu began in 2015 and has since been tirelessly rearing stock to the quality and levels needed to supply the best restaurants and consumers. We combine the origin of Japanese breeding genetics and 200 year old techniques with New Zealand’s grass, grain, water and air.
Website:
https://emberridge-example.co.nz/
Brand Guidelines:
https://brandpages-example.net/view/emberridgebrandguide/home?authuser=0
The smallgoods packaging designs should have consistent branding, with only the product names and colours changing across the designs. The placement of the gold foil needs to be consistent across all the designs.
The packaging dimensions are 17 x 24 cm.
The required components that need to be on the FRONT of the packaging are:
- Our logo
- The product weight
- The product name
The required components that need to be on the BACK of the packaging are:
- Proudly Farmed in New Zealand
- Keep chilled at or below 4°c
- 42 Tannery Lane, Halsworth, Christchurch, New Zealand
- Spaceholder text (we will include some information about the brand)
- Gold medals/badges to emphasize our main selling points
Attached are some drafts as well as our logos. If you need additional imagery or further questions please don't hesitate to contact us at the following emails below:
contact@emberridge-example.co.nz
petra@emberridge-example.co.nz

```html
<!DOCTYPE html>
<html lang="en">
<head>
<meta charset="utf-8">
<title>Ember Ridge Wagyu – Smallgoods Packaging</title>
<link rel="stylesheet" href="https://fonts.googleapis.com/css2?family=Jost:wght@300;400;500;700&display=swap">
<style>
  :root {
    --backdrop: #87a0ab;
    --pack-black: #000000;
    --gold: #ad9170;
    --ember-red: #e8353a;
    --white: #ffffff;
    --meat-light: #d87a78;
    --meat-mid: #c0484e;
    --meat-dark: #9c3038;
  }
  * { margin: 0; padding: 0; box-sizing: border-box; }
  html, body {
    width: 1200px; height: 1200px; overflow: hidden;
    background: var(--backdrop);
    font-family: "Jost", "Century Gothic", sans-serif;
  }
  .canvas { position: relative; width: 1200px; height: 1200px; }

  .pack {
    position: absolute; top: 237px;
    width: 516px; height: 727px;
    background: var(--pack-black);
    overflow: hidden;
  }
  .pack--fina-seca { left: 66px; }
  .pack--bresaola { left: 618px; }

  .pack__corner {
    position: absolute; left: 0; top: 0;
    width: 145px; height: 309px;
  }
  .pack__hanger {
    position: absolute; left: 219px; top: 35px;
    width: 78px; height: 42px;
  }
  .pack__seal {
    position: absolute; left: 382px; top: 36px;
    width: 96px; height: 96px;
  }

  .brand {
    position: absolute; left: 0; right: 0; top: 118px;
    text-align: center;
    color: var(--white);
    font-weight: 700;
    font-size: 34px;
    line-height: 55px;
    letter-spacing: 0.5em;
    text-indent: 0.5em;
  }

  .product-photo {
    position: absolute; left: 83px; top: 250px;
    width: 412px; height: 316px;
    border: 12px solid var(--gold);
  }
  .product-photo__fill {
    width: 100%; height: 100%;
    background: linear-gradient(160deg, var(--meat-light) 0%, var(--meat-mid) 45%, var(--meat-dark) 100%);
  }
  .pack--bresaola .product-photo__fill {
    background: linear-gradient(160deg, #e29a90 0%, #d97a74 50%, #c9605f 100%);
  }

  .name-band {
    position: absolute; left: 0; right: 0; top: 590px; height: 67px;
    border-top: 3px solid var(--gold);
    border-bottom: 3px solid var(--gold);
    display: flex; align-items: center; justify-content: center;
  }
  .product-name {
    color: var(--gold);
    font-weight: 500;
    letter-spacing: 0.03em;
    text-transform: uppercase;
  }
  .name-band .product-name { font-size: 33px; }

  .weight { color: var(--gold); font-weight: 300; }
  .pack--fina-seca .weight {
    position: absolute; left: 0; right: 0; top: 678px;
    text-align: center; font-size: 20px;
  }

  .label-row {
    position: absolute; left: 65px; top: 590px; width: 388px; height: 67px;
  }
  .label-row .product-name {
    position: absolute; left: 0; top: 0;
    font-size: 29px; line-height: 35px;
  }
  .label-row__divider {
    position: absolute; left: 192px; top: 0;
    width: 3px; height: 67px; background: var(--gold);
  }
  .label-row .weight {
    position: absolute; right: 0; top: 8px;
    font-size: 39px; line-height: 40px;
  }
</style>
</head>
<body>
<main class="canvas">

  <section class="pack pack--fina-seca">
    <svg class="pack__hanger" viewBox="0 0 78 42" aria-hidden="true">
      <path d="M12 18 H24 C28 18 29 15 30 10 C31 3 35 0 39 0 C43 0 47 3 48 10 C49 15 50 18 54 18 H66 A12 12 0 0 1 66 42 H12 A12 12 0 0 1 12 18 Z" fill="var(--backdrop)"/>
    </svg>
    <svg class="pack__seal" viewBox="0 0 96 96" aria-hidden="true">
      <circle cx="48" cy="48" r="46.5" fill="none" stroke="var(--gold)" stroke-width="2"/>
      <circle cx="48" cy="48" r="27" fill="none" stroke="var(--gold)" stroke-width="1.5"/>
    </svg>
    <div class="brand">EMBER<br>RIDGE</div>
    <figure class="product-photo">
      <div class="product-photo__fill" role="img" aria-label="Thinly sliced wagyu fina seca with marbling, with a white bull silhouette"></div>
    </figure>
    <div class="name-band"><h2 class="product-name">Wagyu Fina Seca</h2></div>
    <p class="weight">80 g</p>
  </section>

  <section class="pack pack--bresaola">
    <svg class="pack__corner" viewBox="0 0 145 309" aria-hidden="true">
      <polygon points="0,0 145,0 0,309" fill="var(--ember-red)"/>
    </svg>
    <svg class="pack__hanger" viewBox="0 0 78 42" aria-hidden="true">
      <path d="M12 18 H24 C28 18 29 15 30 10 C31 3 35 0 39 0 C43 0 47 3 48 10 C49 15 50 18 54 18 H66 A12 12 0 0 1 66 42 H12 A12 12 0 0 1 12 18 Z" fill="var(--backdrop)"/>
    </svg>
    <svg class="pack__seal" viewBox="0 0 96 96" aria-hidden="true">
      <circle cx="48" cy="48" r="46.5" fill="none" stroke="var(--gold)" stroke-width="2"/>
      <circle cx="48" cy="48" r="27" fill="none" stroke="var(--gold)" stroke-width="1.5"/>
    </svg>
    <div class="brand">EMBER<br>RIDGE</div>
    <figure class="product-photo">
      <div class="product-photo__fill" role="img" aria-label="Overlapping slices of wagyu bresaola, with a white bull silhouette"></div>
    </figure>
    <div class="label-row">
      <h2 class="product-name">Wagyu<br>Bresaola</h2>
      <span class="label-row__divider"></span>
      <p class="weight">80 g</p>
    </div>
  </section>

</main>
</body>
</html>
```